Neukunden-Flyer für Yoga-&Massage
Zielgruppe
Yoga-Leherin, die Yoga nicht nur zur zeitweisen Entspannung vermittelt sondern als Ansatz dauerhafter Entschleunigung, Stressbewältigung und körperlicher Fitness. Thai Yoga Massage arbeitet nicht nur körperlich sondern auch energetisch auch auf der Herzebene.
Zielgruppe:
Jeder, der sich etwas Gutes tun will und seine Selbstheilungskräfte aktivieren und wieder mehr bei sich sein möchte.
Aufgabenstellung
Erstellung eines Flyers mit folgenden Eigenschaften:
• DIN A4 lang - Wickelfalz-Flyer 6-seitig
• Klare Formen und kräftige Farben
• Einprägsam
• Fließend
• CMYK - keine Sonderfarben
• Druckdatenvorlage (PSDs (außen/innen bzw. Druckdatenerstellung Fonts/Pfade
beachten)
Abgabe als offene Datei: PSD, AI bzw. als geschlossene Druckdatei X3 PDF.

```html
<!DOCTYPE html>
<html lang="de">
<head>
<meta charset="utf-8">
<title>LICHTGRUND – Flyer</title>
<link rel="stylesheet" href="https://fonts.googleapis.com/css2?family=Arimo:wght@400;700&display=swap">
<style>
:root{
  --pink:#e2498f;
  --pink-deep:#c9337a;
  --green:#b8cc1a;
  --white:#ffffff;
  --sky-top:#b08a5e;
  --sky-mid:#e2a864;
  --sky-glow:#f6c878;
  --ground:#2a1a10;
  --page:#ffffff;
}
*{margin:0;padding:0;box-sizing:border-box}
html,body{width:907px;height:1200px;overflow:hidden;background:var(--page)}
body{font-family:"Arimo",Arial,sans-serif;color:var(--white)}
.canvas{position:relative;width:907px;height:1200px;overflow:hidden;border:1px solid #333;background:var(--page)}
.sheet{position:absolute;display:flex;overflow:hidden}
.sheet--outside{left:0;top:0;width:826px;height:584px}
.sheet--inside{left:80px;top:615px;width:827px;height:585px}
.panel{position:relative;height:100%;overflow:hidden;flex:none}
.sheet--outside .panel{width:278px}
.sheet--outside .panel:last-child{width:270px}
.sheet--inside .panel{width:271px}
.sheet--inside .panel--mid{width:278px}
.sheet--inside .panel:last-child{width:278px}
.photo-sunset{position:absolute;inset:0;background:
  linear-gradient(180deg,var(--sky-top) 0%,var(--sky-mid) 45%,var(--sky-glow) 80%,#8a5a30 92%,var(--ground) 100%)}
.photo-sunset--glow{background:
  radial-gradient(circle at 55% 72%,#fff3c4 0%,var(--sky-glow) 18%,transparent 45%),
  linear-gradient(180deg,#9a7a52 0%,var(--sky-mid) 40%,var(--sky-glow) 75%,#7a4c26 93%,var(--ground) 100%)}
.panel--pink{background:linear-gradient(180deg,var(--pink) 0%,var(--pink) 85%,var(--pink-deep) 100%)}
.band{position:absolute;left:0;right:0;top:22px;height:54px;background:var(--green);display:flex}
.band span{flex:1;text-align:center;font-weight:700;font-size:16.5px;line-height:54px}
.text{position:absolute;font-size:10.3px;line-height:12.9px}
.text p{margin-bottom:12.9px}
.label{color:var(--green)}
.heading{color:var(--green);font-weight:700;font-size:12.5px;margin-bottom:16px}
.copy-pink{color:var(--pink);font-weight:700}
.copy-pink-light{color:var(--pink)}
.prices{position:absolute;top:495px;font-size:10.3px;line-height:13px;font-weight:700}
.prices .label{font-size:11px}
.brand{position:absolute;left:38px;top:505px;display:flex;align-items:center;gap:8px}
.brand-dot{width:20px;height:20px;border-radius:50%;background:var(--pink)}
.brand-name{color:var(--pink);font-size:18px;letter-spacing:4px}
.inset{position:absolute}
</style>
</head>
<body>
<div class="canvas">

  <section class="sheet sheet--outside">
    <div class="panel">
      <div class="photo-sunset" role="img" aria-label="Sonnenuntergang über dem Meer mit Wolkenhimmel"></div>
      <div class="text" style="left:25px;top:349px;width:245px">
        <p><span class="label">LICHTGRUND</span><br>versteht sich als Kraftquelle<br>für körperliche Fitness, mentale Ruhe und<br>seelisches Gleichgewicht.</p>
        <p><span class="label">Vita</span><br>800 Stunden zertifizierte Sattva-Flow Lehrerin.<br>Ausbildung bei Jonas Weidner und Katrin<br>Holm. Laufende Assistenz bei Stefan<br>Rauch (Ashtanga Studio Süd). Ich unterrichte<br>in München Gruppen- &amp; Einzelkurse – unter<br>anderem in den Yoga-Studios von Jonas<br>Weidner, Yoga-Lehrer der Fußball-National-<br>mannschaft.</p>
      </div>
    </div>
    <div class="panel panel--pink">
      <div class="text" style="left:24px;top:96px;width:245px">
        <p class="heading">TERMIN &amp; KONTAKT</p>
        <p>Vereinbaren Sie noch heute einen Termin<br>und erleben Sie, wie Sie durch individuelle<br>Körperarbeit mehr zu sich selbst finden.</p>
        <p>LICHTGRUND<br>Mara Lindner<br>Feldmochinger Weg 14<br>81379 München<br>E-Mail: hallo@lichtgrund.de<br>Mobil: 0176 - 40215587</p>
        <p>Anreise mit Auto:<br>GUTSHOF ALTBACH - zentral in München<br>Altviertel ggf. Rückseite finden sich fast<br>immer Parkgelegenheiten.</p>
        <p>Anreise mit Bus &amp; Bahn:<br>Die Buslinien 132, N40, N41<br>(Haltestelle Lindenplatz) sowie 53<br>(Haltestelle</p>
        <p>Marktkirche) halten direkt vor der Tür.<br>Nur 5 Minuten zu Fuß sind U3, S7 und S27<br>(Haltestelle Rosenanger) entfernt.</p>
      </div>
    </div>
    <div class="panel">
      <div class="photo-sunset photo-sunset--glow" role="img" aria-label="Silhouette einer Yoga-Übenden im Dreieck vor tiefstehender Sonne"></div>
      <div class="brand"><span class="brand-dot"></span><span class="brand-name">LICHTGRUND</span></div>
    </div>
  </section>

  <section class="sheet sheet--inside">
    <div class="panel">
      <div class="photo-sunset" role="img" aria-label="Sonnenuntergang über dem Meer mit Wolkenhimmel"></div>
      <div class="inset" role="img" aria-label="Foto einer Thai Yoga Massage an Schulter und Rücken" style="left:49px;top:108px;width:81px;height:122px;background:linear-gradient(160deg,#e9e4e2,#8a6a5c)"></div>
      <div class="inset" role="img" aria-label="Foto einer Fußmassage" style="left:135px;top:144px;width:81px;height:121px;background:linear-gradient(160deg,#efe6e2,#c9a998)"></div>
      <div class="text" style="left:24px;top:287px;width:235px;line-height:13px">
        <span class="label" style="font-weight:700">Wann haben Sie sich das letzte Mal in<br>Ihrem Körper zuhause gefühlt?</span><br>
        <span class="copy-pink">Thai Yoga Massage ermöglicht tiefe Rege-<br>neration. Verspannungen und Energieb-<br>lockaden werden durch nährende Berüh-<br>rungen wirkungsvoll gelöst. Die Erfahrung<br>bewegt zu werden umfasst Körper, Seele<br>und Geist. Ein Erlebnis, dass noch lange<br>nachwirkt.<br>Gönnen Sie sich einen ruhigen Raum,<br>Achtsamkeit, Präsenz, Zeit nur für sich.<br>Eine Investition um neue Energie zu<br>tanken.</span>
      </div>
      <div class="prices" style="left:24px"><span class="label">Preise</span><br><span class="copy-pink">Schnupperpreis 60 min / 45 €<br>60 Minuten – 65 €<br>90 Minuten – 85 €<br>120 Minuten – 110 €</span></div>
    </div>
    <div class="panel panel--mid panel--pink">
      <div class="inset" role="img" aria-label="Silhouette einer meditierenden Person im Gras bei Sonnenuntergang" style="left:62px;top:106px;width:151px;height:100px;background:radial-gradient(circle at 50% 55%,#f7c56e,#c98434 55%,#3a2412 100%)"></div>
      <div class="text" style="left:27px;top:246px;width:245px;font-size:10.8px;line-height:14px">
        <p style="margin-bottom:14px">Der Einzelunterricht richtet sich nach Ihren<br>individuellen Zielen und Wünschen.</p>
        <p style="margin-bottom:14px">Ihren Fähigkeiten nach, erarbeiten wir<br>ihre ganz persönliche Übungssequenz.<br>Die Atmung ist der Schlüssel zur bewuss-<br>ten Wahrnehmung.</p>
        <p style="margin-bottom:14px">Steigerung des körperlichen Wohlbefin-<br>dens, Ausgeglichenheit und Widerstands-<br>fähigkeit sind die Folge.</p>
        <p>Jede Stunde endet mit einer 5-minütigen<br>Nackenmassage und anschließender<br>Tiefenentspannung.</p>
      </div>
      <div class="prices" style="left:23px"><span class="label">Preise</span><br>Schnupperpreis 60 min / 55 €<br>60 Minuten – 85 €<br>90 Minuten – 110 €</div>
    </div>
    <div class="panel">
      <div class="photo-sunset photo-sunset--glow" role="img" aria-label="Silhouette einer Yoga-Übenden im Dreieck vor tiefstehender Sonne"></div>
      <div class="text copy-pink-light" style="left:29px;top:358px;width:245px;font-size:10.8px;line-height:14px">Im Coaching lernen Sie mit beruflichen<br>Konflikten und persönlichen Beziehungs-<br>spannungen umzugehen.<br>Ich gebe Ihnen alltagstaugliche Techniken<br>an die Hand um sich für die persönlichen<br>Herausforderungen zu stärken und immer<br>wieder tiefe Ruhepole zu finden.</div>
      <div class="prices" style="left:29px"><span class="label" style="color:var(--pink)">Preise</span><br><span class="copy-pink">Schnupperpreis 60 min / 55 €<br>60 Minuten – 85 €<br>90 Minuten – 110 €</span></div>
    </div>
    <div class="band"><span>Thai Yoga Massage</span><span>Yoga</span><span>Coach</span></div>
  </section>

</div>
</body>
</html>
```